Electrical company business card design.

Hi, were an electrical company in Wellmere New Zealand called Quarneth Ltd. We focus mainly on high end residential and commercial so the card would be targeted towards that.
The card will be for myself, i am the director of the company.
Name: Derek Olstow
Position: Director/electrician
Phone: 021 387 9415
Email: derek@quarneth.co.nz
Location: Auckland
As for colors the the blue color in the logo is preferred, i also don't mind a black background option.
Target Market(s)
High end residential and commercial
Industry/Entity Type
Electrician
Contact Information for Business Card
Name: Derek Olstow Position: Director/Electrician Phone: 021 387 9415, Email: derek@quarneth.co.nz, Location: Auckland

```html
<!DOCTYPE html>
<html lang="en">
<head>
<meta charset="utf-8">
<title>Quarneth Ltd – Business Card</title>
<link rel="stylesheet" href="https://fonts.googleapis.com/css2?family=Jura:wght@500;600;700&display=swap">
<style>
  :root {
    --page: #5a5e62;
    --card: #0d0d0e;
    --card-soft: #1a1a1c;
    --steel: #b9bec4;
    --blue: #1e9be0;
    --blue-deep: #123b5e;
    --gold: #e9bb80;
  }
  * { box-sizing: border-box; margin: 0; padding: 0; }
  html, body {
    width: 1200px; height: 780px; overflow: hidden;
    background: var(--page);
    font-family: "Jura", sans-serif;
  }
  .stage {
    width: 1200px; height: 780px;
    display: flex; align-items: center; justify-content: center; gap: 40px;
  }
  .card {
    position: relative;
    width: 560px; height: 320px;
    border-radius: 22px;
    background: linear-gradient(160deg, var(--card) 0%, var(--card-soft) 100%);
    overflow: hidden;
    box-shadow: 0 14px 30px rgba(0,0,0,.45);
  }

  .front-artwork {
    position: absolute; left: 0; top: 0; width: 360px; height: 320px;
    background: linear-gradient(115deg, var(--blue-deep) 0%, rgba(18,59,94,.55) 45%, rgba(13,13,14,0) 100%);
  }

  .brand { position: absolute; }
  .brand-name {
    font-weight: 700; color: var(--steel);
    letter-spacing: 4px; line-height: 1; white-space: nowrap;
  }
  .brand-tagline {
    font-weight: 600; color: var(--steel);
    text-transform: uppercase; letter-spacing: 2.4px; white-space: nowrap;
  }
  .brand-dot {
    display: inline-block; border-radius: 50%;
    background: var(--blue); vertical-align: middle;
  }

  /* front */
  .front .brand { left: 200px; top: 112px; }
  .front .brand-name { font-size: 46px; }
  .front .brand-dot { width: 16px; height: 16px; margin-right: 12px; }
  .front .brand-tagline { font-size: 13px; margin-top: 10px; padding-left: 30px; }
  .front-url {
    position: absolute; left: 26px; top: 40px;
    writing-mode: vertical-rl;
    color: var(--gold); font-size: 17px; font-weight: 600; letter-spacing: 1px;
  }

  /* back */
  .back .brand { right: 34px; top: 32px; text-align: right; }
  .back .brand-name { font-size: 30px; }
  .back .brand-dot { width: 11px; height: 11px; margin-right: 8px; }
  .back .brand-tagline { font-size: 9px; margin-top: 6px; letter-spacing: 1.8px; }

  .person { position: absolute; left: 40px; top: 120px; }
  .person-name {
    font-size: 28px; font-weight: 600; color: var(--blue);
    letter-spacing: 1.5px; text-transform: uppercase;
    padding-bottom: 4px; border-bottom: 1px solid var(--steel);
    display: inline-block;
  }
  .person-role { font-size: 17px; color: var(--gold); font-weight: 600; margin-top: 6px; }

  .contact-list { position: absolute; left: 40px; top: 200px; list-style: none; }
  .contact-item {
    display: flex; align-items: center; gap: 10px;
    color: var(--gold); font-size: 15px; font-weight: 600; line-height: 24px;
  }
  .contact-icon { width: 13px; height: 13px; fill: var(--gold); flex: none; }
</style>
</head>
<body>
<main class="stage">

  <section class="card front" aria-label="Card front">
    <div class="front-artwork" role="img" aria-label="Decorative blue and grey background artwork"></div>
    <div class="front-url">www.quarneth.com</div>
    <div class="brand">
      <div class="brand-name"><span class="brand-dot"></span>QUARNETH</div>
      <div class="brand-tagline">Wired for excellence</div>
    </div>
  </section>

  <section class="card back" aria-label="Card back">
    <div class="brand">
      <div class="brand-name"><span class="brand-dot"></span>QUARNETH</div>
      <div class="brand-tagline">Wired for excellence</div>
    </div>

    <div class="person">
      <div class="person-name">Derek Olstow</div>
      <div class="person-role">Director Electrician</div>
    </div>

    <ul class="contact-list">
      <li class="contact-item">
        <svg class="contact-icon" viewBox="0 0 24 24" aria-hidden="true"><path d="M6.6 10.8a15.1 15.1 0 0 0 6.6 6.6l2.2-2.2a1 1 0 0 1 1-.25 11.4 11.4 0 0 0 3.6.57 1 1 0 0 1 1 1V20a1 1 0 0 1-1 1A17 17 0 0 1 3 4a1 1 0 0 1 1-1h3.5a1 1 0 0 1 1 1c0 1.25.2 2.45.57 3.57a1 1 0 0 1-.25 1z"/></svg>
        021 387 9415
      </li>
      <li class="contact-item">
        <svg class="contact-icon" viewBox="0 0 24 24" aria-hidden="true"><path d="M2 5h20v14H2z M2 5l10 8 10-8" stroke="var(--card)" stroke-width="1.5"/></svg>
        derek@quarneth.co.nz
      </li>
      <li class="contact-item">
        <svg class="contact-icon" viewBox="0 0 24 24" aria-hidden="true"><circle cx="12" cy="12" r="10" fill="none" stroke="var(--gold)" stroke-width="2"/><path d="M2 12h20M12 2c3 3 3 17 0 20M12 2c-3 3-3 17 0 20" fill="none" stroke="var(--gold)" stroke-width="1.6"/></svg>
        www.quarneth.com
      </li>
      <li class="contact-item">
        <svg class="contact-icon" viewBox="0 0 24 24" aria-hidden="true"><path d="M12 2a7 7 0 0 0-7 7c0 5 7 13 7 13s7-8 7-13a7 7 0 0 0-7-7zm0 9.5A2.5 2.5 0 1 1 12 6.5a2.5 2.5 0 0 1 0 5z"/></svg>
        Wellmere New Zealand
      </li>
    </ul>
  </section>

</main>
</body>
</html>
```